Luxury new home community needs a contemporary and high end looking brochure

We need a brochure to introduce a luxury new home community. The brochure needs to have a modern and high end look and feel while still keeping nature a predominant theme.
The "purpose.doc" describes the text and must have images for each page. The "BrandGuidelines.pdf" includes the color palette. The "11x17 halffold-inside.jpg and 11x17halffold-outside.jpg" files include the print guidelines that must be met.
The additional images downloaded can be used at your discretion-be creative! I prefer Photoshop files please. Additional information about our new home community can be found at www.MaplecrestHollowNB.com

Target Market(s)

High Net Worth Individuals
Real Estate Agents

Industry/Entity Type

Real Estate

Requirements
Must have
• Please see Purpose.doc for required text and images
• Please see BrandGuidelines.pdf for color palette and fonts

```html
<!DOCTYPE html>
<html lang="en">
<head>
<meta charset="utf-8">
<title>Maplecrest Hollow – Brochure Spreads</title>
<link href="https://fonts.googleapis.com/css2?family=Roboto+Condensed:wght@300;400;700&family=Roboto:wght@300;400&display=swap" rel="stylesheet">
<style>
  :root{
    --backdrop:#d8d8d8;
    --frame-light:#a49b94;
    --frame-dark:#6f6760;
    --page:#eeeeef;
    --band:#9d9a98;
    --ink:#1c1d20;
    --ink-soft:#4a4a4c;
    --taupe-text:#6c655f;
    --tab:#14171b;
    --photo-sky:#6f96c4;
    --photo-stone:#8a6a45;
    --forest-deep:#1f3d1c;
    --forest-mid:#3d6a2c;
    --square-gray:#8f8f8f;
    --square-dark:rgba(70,64,58,.82);
    --rule:#222;
  }
  *{margin:0;padding:0;box-sizing:border-box}
  html,body{width:996px;height:1200px;overflow:hidden;background:var(--backdrop)}
  body{position:relative;font-family:"Roboto",sans-serif;color:var(--ink)}

  .spread{position:absolute;left:86px;width:824px;height:534px;overflow:hidden}
  .spread--outside{top:56px}
  .spread--inside{top:610px}
  .spread__frame{position:absolute;inset:0}
  .spread__page{position:absolute;left:24px;top:24px;width:776px;height:486px;background:var(--page)}
  .spread__fold{position:absolute;left:411px;top:24px;width:1px;height:486px;background:rgba(0,0,0,.06)}

  .box{position:absolute}
  .fill-map-street{background:linear-gradient(180deg,#f4f1ea,#e7e2d6);border:3px solid #5d4a2c}
  .fill-map-region{background:linear-gradient(180deg,#f2efe8,#e2ddd2);border:2px solid #5d4a2c}
  .fill-forest{background:linear-gradient(160deg,var(--forest-mid),var(--forest-deep));border:2px solid #333}
  .fill-forest-light{background:linear-gradient(180deg,#8fb46a 0%,#4f7f32 55%,#2e4f22 100%);border:2px solid #333}
  .fill-creek{background:linear-gradient(170deg,#3d5f2a 0%,#2b4420 50%,#8a8577 80%,#5a5648 100%);border:2px solid #333}
  .fill-home{background:linear-gradient(180deg,var(--photo-sky) 0%,#c9d7e6 30%,var(--photo-stone) 50%,#6c5336 72%,#4f8b2e 84%,#3f6f24 100%)}
  .fill-siteplan{background:linear-gradient(150deg,#5f7f52,#2f4c2a 60%,#243d20);border:2px solid #333}

  .located-band{position:absolute;left:24px;top:272px;width:387px;height:156px;background:var(--band)}
  .located__title{position:absolute;left:46px;top:294px;font:700 17px/1 "Roboto Condensed",sans-serif;color:var(--ink)}
  .located__sub{position:absolute;left:46px;top:315px;width:188px;font:300 16px/20px "Roboto Condensed",sans-serif;color:var(--ink);white-space:nowrap}
  .located__body{position:absolute;left:46px;top:360px;width:172px;font:400 7px/9.6px "Roboto",sans-serif;color:var(--ink)}

  .brandmark{position:absolute;left:240px;top:290px;width:140px}
  .brandmark__square{width:56px;height:56px;background:var(--ink)}
  .brandmark__name{margin-top:6px;font:700 16px/1.05 "Roboto Condensed",sans-serif;color:var(--ink);letter-spacing:.3px}
  .brandmark__partner{margin-top:6px;font:700 11px/1.15 "Roboto Condensed",sans-serif;color:var(--ink);letter-spacing:.8px}

  .contact{position:absolute;left:24px;width:387px;text-align:center}
  .contact__phone{top:450px;font:700 22px/1 "Roboto Condensed",sans-serif;color:var(--taupe-text)}
  .contact__web{top:478px;font:300 19px/1 "Roboto",sans-serif;color:var(--ink)}

  .intro{position:absolute;left:442px;top:56px;color:var(--taupe-text)}
  .intro__lead{font:300 16px/21px "Roboto",sans-serif}
  .intro__title{font:700 17px/21px "Roboto Condensed",sans-serif}

  .deco{position:absolute}
  .deco--a{left:652px;top:108px;width:58px;height:56px;background:var(--square-dark)}
  .deco--b{left:682px;top:142px;width:77px;height:78px;background:var(--square-dark)}
  .deco--c{left:666px;top:329px;width:86px;height:86px;background:var(--square-gray)}
  .deco--d{left:751px;top:416px;width:25px;height:24px;background:var(--tab)}

  .lots{position:absolute;left:442px;top:378px;color:var(--taupe-text)}
  .lots__count{font:300 27px/1 "Roboto",sans-serif;letter-spacing:.5px}
  .lots__desc{margin-top:4px;font:300 19px/1 "Roboto",sans-serif}

  .price-tab{position:absolute;left:411px;top:460px;width:237px;height:30px;background:var(--tab);clip-path:polygon(0 0,100% 0,95% 100%,0 100%)}
  .price-tab__text{position:absolute;left:30px;top:7px;font:300 14px/1 "Roboto",sans-serif;color:#fff}

  .lot-table{position:absolute;left:300px;top:36px;width:99px;height:352px;display:grid;
    grid-template-columns:22px 1fr 33px;grid-template-rows:repeat(37,1fr);gap:1px;padding:1px;background:var(--rule);
    font:400 9px/1 Arial,sans-serif;color:#111}
  .lot-table span{background:#fff;display:flex;align-items:center;justify-content:center;overflow:hidden}
  .lot-table span.num{justify-content:flex-start;padding-left:5px}

  .feature{position:absolute;left:442px;width:330px}
  .feature__head{font:300 17px/1 "Roboto Condensed",sans-serif;color:var(--ink);display:flex;align-items:center;gap:6px}
  .feature__head strong{font-weight:700}
  .feature__arrow{width:7px;height:9px}
  .feature__body{margin-top:7px;font:400 7px/9.6px "Roboto",sans-serif;color:var(--ink-soft)}
</style>
</head>
<body>

<section class="spread spread--outside">
  <svg class="spread__frame" width="824" height="534" viewBox="0 0 824 534">
    <rect width="824" height="534" fill="var(--frame-light)"/>
    <polygon points="0,150 411,120 411,534 0,534" fill="var(--frame-dark)"/>
    <polygon points="411,0 824,0 824,534 411,534" fill="var(--frame-light)"/>
    <polygon points="700,534 824,430 824,534" fill="var(--frame-dark)"/>
  </svg>
  <div class="spread__page"></div>

  <div class="box fill-map-street" style="left:43px;top:42px;width:222px;height:202px" role="img" aria-label="Street map showing the community location near Route 9 and 140th Street"></div>
  <div class="box fill-map-region" style="left:273px;top:42px;width:122px;height:98px" role="img" aria-label="Regional highway map with the community marked"></div>
  <div class="box fill-forest" style="left:273px;top:146px;width:122px;height:98px" role="img" aria-label="Aerial photo of dense forest canopy"></div>

  <div class="located-band"></div>
  <h2 class="located__title">Conveniently located</h2>
  <p class="located__sub">¼ mile west of Route 9 on<br>140th Street, Brookhaven, NB</p>
  <p class="located__body">The peaceful enclave of Maplecrest Hollow is nestled in the heart of the Route 9 growth corridor, giving homeowners convenient access to shops, services, dining, entertainment and recreation throughout Cedar County and the larger Riverton metro area.</p>

  <div class="brandmark">
    <div class="brandmark__square"></div>
    <div class="brandmark__name">MAPLECREST HOLLOW</div>
    <div class="brandmark__partner">SUMMIT CREST DEVELOPMENT</div>
  </div>

  <p class="contact contact__phone">(402) 555-0148</p>
  <p class="contact contact__web">MaplecrestHollowNB.com</p>

  <div class="intro">
    <p class="intro__lead">Introducing Brookhaven’s newest</p>
    <p class="intro__title">Luxury New Home<br>Community</p>
  </div>

  <div class="box fill-home" style="left:442px;top:128px;width:268px;height:244px" role="img" aria-label="Photo of a stone luxury home with a green lawn under a blue cloudy sky"></div>
  <div class="deco deco--a"></div>
  <div class="deco deco--b"></div>
  <div class="deco deco--c"></div>
  <div class="deco deco--d"></div>

  <div class="lots">
    <p class="lots__count">36 HEAVILY</p>
    <p class="lots__desc">Wooded Estate Sized Lots</p>
  </div>

  <div class="price-tab"><span class="price-tab__text">Custom Homes from $1 Million</span></div>
  <div class="spread__fold"></div>
</section>

<section class="spread spread--inside">
  <svg class="spread__frame" width="824" height="534" viewBox="0 0 824 534">
    <rect width="824" height="534" fill="var(--frame-dark)"/>
    <polygon points="0,0 411,0 411,60 0,110" fill="var(--frame-light)"/>
    <polygon points="411,0 824,0 824,534 411,534" fill="var(--frame-light)"/>
    <polygon points="780,534 824,500 824,534" fill="var(--frame-dark)"/>
  </svg>
  <div class="spread__page"></div>

  <div class="box fill-siteplan" style="left:35px;top:34px;width:254px;height:354px" role="img" aria-label="Aerial site plan of 36 wooded lots, curving streets, pavilion and 11 acre private park"></div>

  <div class="lot-table" role="table" aria-label="Lot sizes">
    <span>Lot</span><span>Sq. Ft.</span><span>Acres</span>
    <span>1</span><span class="num">26,025</span><span>.60</span>
    <span>2</span><span class="num">23,890</span><span>.55</span>
    <span>3</span><span class="num">28,154</span><span>.65</span>
    <span>4</span><span class="num">30,171</span><span>.69</span>
    <span>5</span><span class="num">46,975</span><span>1.08</span>
    <span>6</span><span class="num">32,826</span><span>.75</span>
    <span>7</span><span class="num">26,585</span><span>.61</span>
    <span>8</span><span class="num">35,498</span><span>.81</span>
    <span>9</span><span class="num">34,031</span><span>.78</span>
    <span>10</span><span class="num">34,732</span><span>.80</span>
    <span>11</span><span class="num">38,724</span><span>.89</span>
    <span>12</span><span class="num">41,990</span><span>.96</span>
    <span>13</span><span class="num">50,097</span><span>1.15</span>
    <span>14</span><span class="num">28,083</span><span>.64</span>
    <span>15</span><span class="num">31,083</span><span>.71</span>
    <span>16</span><span class="num">29,006</span><span>.67</span>
    <span>17</span><span class="num">31,947</span><span>.73</span>
    <span>18</span><span class="num">27,069</span><span>.62</span>
    <span>19</span><span class="num">29,588</span><span>.68</span>
    <span>20</span><span class="num">30,667</span><span>.70</span>
    <span>21</span><span class="num">30,954</span><span>.71</span>
    <span>22</span><span class="num">35,102</span><span>.81</span>
    <span>23</span><span class="num">54,735</span><span>1.26</span>
    <span>24</span><span class="num">55,075</span><span>1.26</span>
    <span>25</span><span class="num">30,702</span><span>.70</span>
    <span>26</span><span class="num">23,147</span><span>.53</span>
    <span>27</span><span class="num">20,961</span><span>.48</span>
    <span>28</span><span class="num">21,615</span><span>.50</span>
    <span>29</span><span class="num">22,711</span><span>.52</span>
    <span>30</span><span class="num">20,372</span><span>.47</span>
    <span>31</span><span class="num">27,990</span><span>.64</span>
    <span>32</span><span class="num">66,296</span><span>1.52</span>
    <span>33</span><span class="num">30,491</span><span>.70</span>
    <span>34</span><span class="num">79,393</span><span>1.82</span>
    <span>35</span><span class="num">27,907</span><span>.64</span>
    <span>36</span><span class="num">29,977</span><span>.69</span>
  </div>

  <div class="box fill-forest-light" style="left:35px;top:394px;width:180px;height:106px" role="img" aria-label="Photo of sunlit woodland with tall trees"></div>
  <div class="box fill-creek" style="left:221px;top:394px;width:179px;height:106px" role="img" aria-label="Photo of a rocky creek winding through the woods"></div>

  <article class="feature" style="top:62px">
    <h3 class="feature__head"><svg class="feature__arrow" viewBox="0 0 7 9"><polygon points="0,0 7,4.5 0,9" fill="var(--ink)"/></svg><span><strong>Nature</strong> Drives Design</span></h3>
    <p class="feature__body">Maplecrest Hollow offers a different approach to residential development and building. Rather than nature as a hastily landscaped afterthought, it’s instead the driving force behind the community’s planning and construction. 36 homesites averaging over ¾ of an acre have been carefully carved out of heavily wooded terrain, creating a secluded retreat that celebrates the full bounty of this extraordinary property.</p>
  </article>

  <article class="feature" style="top:150px">
    <h3 class="feature__head"><svg class="feature__arrow" viewBox="0 0 7 9"><polygon points="0,0 7,4.5 0,9" fill="var(--ink)"/></svg><span><strong>Preservation</strong> and Conservation</span></h3>
    <p class="feature__body">15’ Side yard buffer zones and tree preservation easements have been created to preserve the natural landscape throughout the community. Plantings shall reinforce the natural character of the community and minimize property line delineation giving homeowners incredible views of untouched areas of nature.</p>
  </article>

  <div class="box fill-forest-light" style="left:442px;top:222px;width:159px;height:100px" role="img" aria-label="Photo of a grassy clearing framed by green trees"></div>
  <div class="box fill-creek" style="left:610px;top:222px;width:160px;height:100px" role="img" aria-label="Photo of a shaded stream bed in the forest"></div>

  <article class="feature" style="top:347px">
    <h3 class="feature__head"><svg class="feature__arrow" viewBox="0 0 7 9"><polygon points="0,0 7,4.5 0,9" fill="var(--ink)"/></svg><span><strong>11 Acre</strong> Private Park</span></h3>
    <p class="feature__body">Amid the majesty of mature trees and the cheerful burble of a meandering stream, over 11 acres of pristine native habitat have been preserved and protected for residents to enjoy. A paved walking trail and pavilion have been carefully planned to create a space accommodating both recreation and reflection.</p>
  </article>

  <article class="feature" style="top:427px">
    <h3 class="feature__head"><svg class="feature__arrow" viewBox="0 0 7 9"><polygon points="0,0 7,4.5 0,9" fill="var(--ink)"/></svg><span><strong>Custom</strong> Homes</span></h3>
    <p class="feature__body">Homeowner’s are encouraged to bring their own custom builder or work with one on our thoughtfully selected team in order to create a dream home that complements and enhances the picturesque surroundings. Estate sized lots allow for creativity in design and construction for those looking for a home that is truly unique.</p>
  </article>

  <div class="spread__fold"></div>
</section>

</body>
</html>
```